Certificate of Completion - Educational Trainings

We are looking for a certificate of completion for individuals who complete one of our specific trainings. Files should be provided in a Word (docx) or PowerPoint (pptx) format. The "Talmoray example.png" file is to show necessary information. Copies of logos have been included for design purposes.

Target Market(s)

Training Participants

Industry/Entity Type

Healthcare

Font styles to use
Sans Serif

```html
<!DOCTYPE html>
<html lang="en">
<head>
<meta charset="utf-8">
<title>Talmoray Certificate of Completion</title>
<link rel="stylesheet" href="https://fonts.googleapis.com/css2?family=Great+Vibes&family=Montserrat:wght@700;800&family=Outfit:wght@600&family=Roboto+Condensed:ital,wght@1,400&family=Roboto:ital,wght@0,300;0,400;0,700;1,400&display=swap">
<style>
  :root {
    --page-bg: #f1f2f4;
    --header-bg: #e5eedc;
    --green-dark: #16703a;
    --green-light: #6ab04c;
    --ink: #111111;
    --panel: #ffffff;
  }
  * { margin: 0; padding: 0; box-sizing: border-box; }
  html, body { width: 1200px; height: 1000px; overflow: hidden; background: var(--page-bg); }
  body { position: relative; font-family: "Roboto", sans-serif; color: var(--ink); }

  .certificate {
    position: absolute; left: 205px; top: 194px; width: 791px; height: 612px;
    background: var(--header-bg);
    box-shadow: 0 8px 22px rgba(0,0,0,0.18);
  }
  .brand { position: absolute; left: 0; width: 400px; top: 114px; text-align: center; }
  .brand-name {
    font-family: "Montserrat", sans-serif; font-weight: 800; font-size: 29px; line-height: 34px;
    letter-spacing: 2px; color: var(--ink);
  }
  .brand-name::before {
    content: ""; display: inline-block; width: 16px; height: 16px; border-radius: 50%;
    background: var(--green-dark); margin-right: 10px; vertical-align: 3px;
  }
  .brand-details { margin-top: 2px; font-weight: 300; font-size: 11.5px; line-height: 14.5px; letter-spacing: 0.2px; }

  .title { position: absolute; left: 330px; top: 0; width: 440px; height: 210px; font-weight: normal; }
  .title-script {
    position: absolute; left: 0; top: 62px; width: 100%; text-align: center;
    font-family: "Great Vibes", cursive; font-size: 100px; line-height: 1;
    color: var(--green-dark); white-space: nowrap;
  }
  .title-sub {
    position: absolute; left: 0; top: 146px; width: 100%; text-align: center;
    font-family: "Montserrat", sans-serif; font-weight: 700; font-size: 41px; line-height: 1;
    color: var(--green-light); letter-spacing: 0.3px; white-space: nowrap;
  }

  .panel {
    position: absolute; left: 8px; top: 221px; width: 776px; height: 368px;
    background: var(--panel); border-radius: 24px 24px 0 0;
  }
  .panel-frame { position: absolute; left: 0; top: 0; width: 776px; height: 368px; }

  .awarded {
    position: absolute; top: 46px; width: 100%; text-align: center;
    font-family: "Outfit", sans-serif; font-weight: 600; font-size: 27px;
  }
  .recipient {
    position: absolute; top: 108px; width: 100%; text-align: center;
    font-family: "Great Vibes", cursive; font-size: 64px; line-height: 1; color: var(--green-dark);
    white-space: nowrap;
  }
  .recipient-rule {
    position: absolute; left: 214px; top: 166px; width: 345px; height: 1.5px; background: var(--green-dark);
  }
  .course {
    position: absolute; top: 193px; width: 100%; text-align: center;
    font-family: "Roboto Condensed", sans-serif; font-style: italic; font-size: 21px; line-height: 23px;
  }
  .completion { position: absolute; left: 50px; top: 332px; font-weight: 300; font-size: 12px; letter-spacing: 0.3px; }
  .completion-date { font-size: 17px; margin-left: 2px; }
  .signatory { position: absolute; left: 589px; top: 317px; text-align: left; }
  .signatory-name {
    font-weight: 700; font-size: 18px; letter-spacing: -0.3px;
    border-bottom: 1.5px solid var(--ink); line-height: 19px;
  }
  .signatory-role { font-weight: 300; font-size: 12px; margin-top: 1px; }

  .footer-band {
    position: absolute; left: 0; bottom: 0; width: 791px; height: 26px;
    background: var(--green-dark); border-radius: 4px 4px 0 0;
    color: #ffffff; font-family: "Roboto", sans-serif; font-style: italic; font-size: 10.3px;
    display: flex; align-items: center; justify-content: center; letter-spacing: 0.1px;
  }
</style>
</head>
<body>
  <main class="certificate">
    <header class="brand">
      <div class="brand-name">TALMORAY</div>
      <div class="brand-details">
        48 HARBOR LANE, STE. 310 BROOKHAVEN, ME 04290<br>
        ALLIED BOARD SPONSOR NUMBER 58213
      </div>
    </header>

    <h1 class="title">
      <span class="title-script">Certificate</span>
      <span class="title-sub">of completion</span>
    </h1>

    <section class="panel">
      <svg class="panel-frame" viewBox="0 0 776 368" role="img" aria-label="Leaf chain ornamental border in dark and light green">
        <path d="M8 368 V28 Q8 8 28 8 H748 Q768 8 768 28 V368" fill="none" stroke="#3f8a45" stroke-width="5"/>
      </svg>
      <p class="awarded">This Certificate Is Awarded To</p>
      <p class="recipient">Marcus Delwyneth</p>
      <div class="recipient-rule"></div>
      <p class="course">
        FOR SUCCESSFUL COMPLETION OF<br>
        BEST PRACTICES: BUDGET PROCESS/BUDGET BUILDING<br>
        COMPLETED ONLINE FIELD OF STUDY FINANCE<br>
        CPE CREDITS: 1
      </p>
      <p class="completion">COMPLETION DATE : <span class="completion-date">05/16/2024</span></p>
      <div class="signatory">
        <div class="signatory-name">NORA HALVICK</div>
        <div class="signatory-role">SENIOR CONSULTANT</div>
      </div>
    </section>

    <footer class="footer-band">IN ACCORDANCE WITH THE STANDARD OF THE ALLIED BOARD OF CPE PROVIDERS, CPE CREDITS HAVE BEEN GRANTED BASED ON A 50 MINUTE HOUR.</footer>
  </main>
</body>
</html>
```